Postcard Flyer For Plumbing Company

We are a p[professional plumbing company in NSW that carry out plumbing, electrical and hot water system work.
i want to send a postcard size flyer 105mm x 148mm to our clients to offer $xx off their next job they book with us.
The front of the flyer needs to say.... Feel The Love WIth $35 Off your Next Job. It needs to include a section where their name and postal address can go (74mm W x 24mm H) on the left hand side of the bottom of the flyer - refer attached example.
The other side of the flyer needs to have a section for text, the offer ($35 or $xx what they get off their next job) and also can use the tag line... Call 1 Number for The Best In 3 Trades - Plumbing, Hot Water & Electrical.
Plumbing, hot water and electrical pictures/icons can be used.
I want the flyer to stand out, use the corporate colours and be modern whilst letting them know that they can use this voucher on their next job.
Refer attachments.

Target Market(s)

Homeowners and our existing clients

Industry/Entity Type

Plumbing

Font styles to use
Serif

Colors
0255a3
ec1f27
ffffff
d3d3d3

Requirements
Must have
• Corporate colours and logos
• Red Colour:
• C=0
• M=100
• Y=100
• K=0
• Blue Colour
• C= 100
• M=66
• Y=0
• K=2
• Grey Colour
• C= 26
• M=21
• Y=19
• K=0
Nice to have
• predominately white background
Should not have
• Black background and lots of black.

```html
<!DOCTYPE html>
<html lang="en">
<head>
<meta charset="utf-8">
<title>Harbor Trades Postcard Flyer</title>
<link rel="stylesheet" href="https://fonts.googleapis.com/css2?family=Montserrat:wght@500;600;700;800&family=Oswald:wght@600;700&display=swap">
<style>
  :root{
    --blue:#0255a3;
    --blue-bright:#1a6fd8;
    --red:#ec1f27;
    --white:#ffffff;
    --grey:#d3d3d3;
    --panel:#f1f1f1;
    --navy:#1c2f5a;
    --ink:#1e1e1e;
    --stage:#e4e4e4;
  }
  *{margin:0;padding:0;box-sizing:border-box}
  html,body{width:1200px;height:771px;overflow:hidden;background:var(--stage);font-family:"Montserrat",Arial,sans-serif}
  .canvas{position:relative;width:1200px;height:771px}
  .flyer{position:absolute;top:41px;width:489px;height:689px;background:var(--panel);overflow:hidden;box-shadow:0 4px 14px rgba(0,0,0,.18)}
  .flyer--back{left:73px}
  .flyer--front{left:635px}
  .photo{position:absolute}
  .bands{position:absolute;left:0;top:0;width:489px;height:689px}

  /* back side */
  .photo--hardhat{left:0;top:0;width:489px;height:345px;background:linear-gradient(120deg,#e9e4dc 0%,#d9d4cc 45%,#c7c3bd 100%)}
  .photo--faucet{left:225px;top:355px;width:264px;height:305px;background:linear-gradient(160deg,#f4f4f2 0%,#dcdcdc 50%,#2a3350 100%)}
  .offer-top{position:absolute;left:306px;top:38px;line-height:1}
  .offer-top .lead{color:var(--red);font-weight:800;font-size:26px;letter-spacing:.5px}
  .offer-top .small{color:var(--ink);font-weight:600;font-size:21px;margin-top:2px}
  .offer-top .amount{font-family:"Oswald",Arial,sans-serif;color:var(--blue-bright);font-weight:700;font-size:41px;margin-top:2px}
  .offer-top .amount span{color:var(--red)}
  .offer-top .tail{color:var(--red);font-weight:800;font-size:26px}
  .service-icon{position:absolute;border-radius:50%;border:3px solid var(--red);background:radial-gradient(circle,#ffffff 30%,#d9d9d9 100%)}
  .brand{position:absolute}
  .brand__name{display:flex;align-items:center;gap:7px;color:var(--navy);font-weight:800;font-size:21px;letter-spacing:.5px}
  .brand__mark{width:12px;height:12px;background:var(--red);border-radius:50%}
  .brand__trades{font-size:9px;font-weight:600;color:var(--ink);margin-top:6px}
  .services-pill{position:absolute;left:29px;top:439px;width:177px;height:31px;border-radius:16px;background:var(--blue);color:var(--white);font-weight:800;font-size:18px;text-align:center;line-height:31px}
  .services-list{position:absolute;left:43px;top:485px;list-style:none}
  .services-list li{display:flex;align-items:center;gap:10px;font-size:18px;font-weight:500;color:var(--ink);height:32px}
  .services-list svg{width:16px;height:16px}
  .call-now{position:absolute;left:34px;top:601px;color:var(--red);font-weight:800;font-size:24px}
  .contact{position:absolute;color:var(--white);display:flex;align-items:center;gap:8px}
  .contact svg{width:13px;height:13px}
  .contact--phone{left:34px;top:640px;font-size:17px;font-weight:700}
  .contact--mail{left:34px;top:666px;font-size:13px;font-weight:500}
  .contact--web{left:278px;top:667px;font-size:13px;font-weight:500}

  /* front side */
  .photo--van{left:0;top:0;width:489px;height:380px;background:linear-gradient(110deg,#f2f2f2 0%,#e3e6ea 45%,#2f58a8 62%,#8a9a6a 85%,#a39a80 100%)}
  .coupon{position:absolute;left:35px;top:446px;width:266px;height:118px;border:2px dashed var(--red);text-align:center;padding-top:8px;line-height:1}
  .coupon .line{color:var(--blue);font-weight:800;font-size:26px}
  .coupon .deal{font-family:"Oswald",Arial,sans-serif;color:var(--red);font-weight:700;font-size:38px;margin:4px 0 5px}
  .tagline{position:absolute;right:28px;top:372px;text-align:right;line-height:1}
  .tagline .call{color:var(--red);font-weight:800;font-size:30px}
  .tagline .number{color:var(--blue);font-weight:800;font-size:30px;margin-top:4px}
  .tagline .best{color:var(--red);font-weight:500;font-size:19px;margin-top:8px}
  .tagline .best b{font-weight:700}
  .tagline .trades{color:var(--red);font-weight:500;font-size:19px;margin-top:6px}
  .tagline .list{color:var(--blue);font-weight:800;font-size:19px;margin-top:6px;line-height:1.3}
  .address-box{position:absolute;left:0;top:576px;width:344px;height:113px;background:var(--white)}
  .phone-bar{position:absolute;left:344px;top:658px;width:145px;height:31px;background:var(--blue);color:var(--white);font-size:12px;font-weight:700;display:flex;align-items:center;justify-content:center;gap:6px}
  .phone-bar svg{width:11px;height:11px}
</style>
</head>
<body>
<div class="canvas">

  <!-- Back side -->
  <section class="flyer flyer--back">
    <div class="photo photo--hardhat" role="img" aria-label="Photo of a smiling tradesman in a hard hat and plaid shirt holding pliers"></div>
    <div class="photo photo--faucet" role="img" aria-label="Photo of a plumber in a navy t-shirt holding a tap and wrench in a kitchen"></div>

    <svg class="bands" viewBox="0 0 489 689" aria-hidden="true">
      <polygon points="0,198 150,272 0,322" fill="var(--blue-bright)"/>
      <polygon points="0,322 150,272 300,318 489,268 489,300 130,406 0,355" fill="var(--white)"/>
      <polygon points="0,355 130,406 489,300 489,352 225,400 225,355 0,345" fill="var(--white)"/>
      <line x1="0" y1="354" x2="132" y2="402" stroke="var(--red)" stroke-width="2"/>
      <polygon points="132,402 489,305 489,318 175,400" fill="var(--red)"/>
      <polygon points="175,400 489,318 489,345 225,398" fill="var(--blue-bright)"/>
      <polygon points="0,632 238,632 258,689 0,689" fill="var(--red)"/>
      <polygon points="258,660 489,660 489,689 268,689" fill="var(--blue)"/>
    </svg>

    <div class="offer-top">
      <div class="lead">CALL NOW</div>
      <div class="small">&amp; GET</div>
      <div class="amount">$200 <span>OFF</span></div>
      <div class="small">ON YOUR</div>
      <div class="tail">NEXT JOB</div>
    </div>

    <div class="service-icon" role="img" aria-label="Pipe fitting icon" style="left:234px;top:285px;width:68px;height:68px"></div>
    <div class="service-icon" role="img" aria-label="Light bulb icon" style="left:301px;top:259px;width:82px;height:82px"></div>
    <div class="service-icon" role="img" aria-label="Hot water tap icon" style="left:373px;top:224px;width:94px;height:94px"></div>

    <div class="brand" style="left:60px;top:300px">
      <div class="brand__name"><span class="brand__mark"></span>HARBOR TRADES</div>
      <div class="brand__trades">Plumbing • Electrical • Hot Water</div>
    </div>

    <div class="services-pill">OUR SERVICES</div>
    <ul class="services-list">
      <li><svg viewBox="0 0 16 16"><path d="M2 9l4 4 8-11" fill="none" stroke="var(--red)" stroke-width="2.4"/></svg>PLUMBING</li>
      <li><svg viewBox="0 0 16 16"><path d="M2 9l4 4 8-11" fill="none" stroke="var(--red)" stroke-width="2.4"/></svg>ELECTRICAL</li>
      <li><svg viewBox="0 0 16 16"><path d="M2 9l4 4 8-11" fill="none" stroke="var(--red)" stroke-width="2.4"/></svg>HOT WATER</li>
    </ul>

    <div class="call-now">CALL NOW</div>
    <div class="contact contact--phone"><svg viewBox="0 0 16 16"><circle cx="8" cy="8" r="7" fill="none" stroke="var(--white)" stroke-width="1.4"/><path d="M5.5 4.5l1.5 1.6-.8 1.2a5 5 0 002.5 2.5l1.2-.8 1.6 1.5-1 1.2c-3 0-6-3-6-6z" fill="var(--white)"/></svg>1-555-010-0199</div>
    <div class="contact contact--mail"><svg viewBox="0 0 16 16"><rect x="1.5" y="3.5" width="13" height="9" fill="none" stroke="var(--white)" stroke-width="1.3"/><path d="M1.5 3.5l6.5 5 6.5-5" fill="none" stroke="var(--white)" stroke-width="1.3"/></svg>hello@harbortrades.com</div>
    <div class="contact contact--web"><svg viewBox="0 0 16 16"><circle cx="8" cy="8" r="6.5" fill="none" stroke="var(--white)" stroke-width="1.3"/><ellipse cx="8" cy="8" rx="3" ry="6.5" fill="none" stroke="var(--white)" stroke-width="1.1"/><line x1="1.5" y1="8" x2="14.5" y2="8" stroke="var(--white)" stroke-width="1.1"/></svg>www.harbortrades.com</div>
  </section>

  <!-- Front side -->
  <section class="flyer flyer--front">
    <div class="photo photo--van" role="img" aria-label="Photo of a smiling technician in blue overalls carrying a toolbox and hose beside a white work van"></div>

    <svg class="bands" viewBox="0 0 489 689" aria-hidden="true">
      <polygon points="0,198 150,272 0,322" fill="var(--blue-bright)"/>
      <polygon points="0,322 150,272 300,318 489,268 489,689 0,689" fill="var(--panel)"/>
      <polygon points="0,322 150,272 300,318 200,360 130,402 0,355" fill="var(--white)"/>
      <line x1="0" y1="354" x2="132" y2="402" stroke="var(--red)" stroke-width="2"/>
      <polygon points="132,402 489,268 489,300 190,400" fill="var(--red)"/>
      <polygon points="190,400 489,300 489,344 150,404" fill="var(--blue-bright)"/>
    </svg>

    <div class="brand" style="left:60px;top:300px">
      <div class="brand__name"><span class="brand__mark"></span>HARBOR TRADES</div>
      <div class="brand__trades">Plumbing • Electrical • Hot Water</div>
    </div>

    <div class="tagline">
      <div class="call">CALL</div>
      <div class="number">1 NUMBER</div>
      <div class="best">for The <b>Best</b></div>
      <div class="trades">In 3 Trades</div>
      <div class="list">PLUMBING,<br>HOT WATER &amp;<br>ELECTRICAL</div>
    </div>

    <div class="coupon">
      <div class="line">FEEL THE LOVE</div>
      <div class="deal">WITH $35 OFF</div>
      <div class="line">YOUR NEXT JOB</div>
    </div>

    <div class="address-box"></div>
    <div class="phone-bar"><svg viewBox="0 0 16 16"><circle cx="8" cy="8" r="7" fill="none" stroke="var(--white)" stroke-width="1.4"/><path d="M5.5 4.5l1.5 1.6-.8 1.2a5 5 0 002.5 2.5l1.2-.8 1.6 1.5-1 1.2c-3 0-6-3-6-6z" fill="var(--white)"/></svg>1-555-010-0199</div>
  </section>

</div>
</body>
</html>
```